Celestine Varga Gymnastics Center Business Card

Develop a business card with my CV logo provided. A classy and unique design using the colors black, white, purple and maybe a splash of gold. Add Address (918 S. Harlan Lane Ashgrove, Indiana 44871), email (CelestineVargaGymnasticsCtr@mailbrook.com, website (www.CelestineVargaGymnasticsCenter.com), phone number (330-555-0192) on the card. Social media if there's room also. t: @VargaGym, i: @VargaGym, f: @CelestineVargaGymnasticsCenter

Target Market(s)

Families, children, gymnastics community and beyond

Industry/Entity Type

Business

Contact Information for Business Card

Add name (Celestine Varga) who is the owner. Add logo, add address details, classy font, uniqueness important, rounded edges on business card. Horizontal business card needed.

Font styles to use
Serif
Sans Serif

Colors
6b449b
ffffff

Requirements
Must have
• Must have logo, owner name and owner on card, must have colors purple, white, black where needed in print, and a splash of gold if appropriate. Keep card classy and clean. Must have address of location, phone number, website of business, email and social media.
Nice to have
• I am open here, but I'd appreciate uniqueness. Must be a lasting image for branding...
Should not have
• No kid-like looks...

```html
<!DOCTYPE html>
<html lang="en">
<head>
<meta charset="utf-8">
<title>Celestine Varga Gymnastics Center – Business Card</title>
<link rel="stylesheet" href="https://fonts.googleapis.com/css2?family=Open+Sans:wght@400;600;700&family=Cormorant+Garamond:wght@500&display=swap">
<style>
  :root {
    --purple: #6b449b;
    --purple-deep: #5e2b8a;
    --purple-soft: #7a55a8;
    --white: #ffffff;
    --paper: #f1f1f1;
    --ink: #1d1d1d;
    --backdrop: #e4e2e8;
  }
  * { box-sizing: border-box; margin: 0; padding: 0; }
  html, body { width: 1200px; height: 900px; overflow: hidden; }
  body {
    background: var(--backdrop);
    font-family: "Open Sans", Arial, sans-serif;
    position: relative;
  }
  .card {
    position: absolute;
    left: 250px;
    width: 700px;
    height: 400px;
    border-radius: 34px;
    overflow: hidden;
    box-shadow: 0 10px 26px rgba(0,0,0,.18);
  }

  /* back side */
  .card-back {
    top: 35px;
    background: radial-gradient(ellipse at 55% 40%, #6a2f97 0%, var(--purple-deep) 70%);
    color: var(--white);
  }
  .card-back .figure-faint {
    position: absolute;
    left: 40px; top: 0;
    width: 200px; height: 400px;
    border-radius: 90px 90px 0 0;
    background: linear-gradient(180deg, rgba(255,255,255,.10), rgba(255,255,255,.04));
  }
  .card-back .monogram {
    position: absolute;
    left: 0; right: 0; top: 120px;
    text-align: center;
    font-size: 96px;
    font-weight: 600;
    letter-spacing: 4px;
    color: var(--white);
  }
  .social-row {
    position: absolute;
    left: 34px; bottom: 34px;
    display: flex;
    align-items: center;
    gap: 10px;
    font-size: 15px;
  }
  .social-row .mark {
    width: 15px; height: 15px;
    background: var(--white);
    border-radius: 3px;
    display: inline-block;
  }
  .social-row .sep { opacity: .9; }

  /* front side */
  .card-front {
    top: 470px;
    background: linear-gradient(120deg, var(--white) 0%, var(--paper) 100%);
    color: var(--ink);
  }
  .brand {
    position: absolute;
    left: 46px; top: 32px;
    width: 270px;
  }
  .brand-mark {
    font-size: 64px;
    font-weight: 600;
    color: var(--ink);
    line-height: 1;
    padding-left: 40px;
  }
  .brand-name {
    margin-top: 6px;
    font-size: 15px;
    font-weight: 600;
    text-transform: uppercase;
    letter-spacing: 1px;
    line-height: 1.2;
    color: var(--ink);
  }
  .brand-tagline {
    margin-top: 4px;
    padding-top: 3px;
    border-top: 1px solid var(--purple);
    font-family: "Cormorant Garamond", Georgia, serif;
    font-size: 15px;
    color: var(--purple);
  }
  .owner {
    position: absolute;
    left: 46px; top: 188px;
  }
  .owner-name {
    font-size: 25px;
    font-weight: 700;
    color: var(--purple);
  }
  .owner-role { font-size: 18px; color: #333; }
  .contact {
    position: absolute;
    left: 46px; top: 268px;
    list-style: none;
    font-size: 16.5px;
    line-height: 25px;
  }
  .contact li { display: flex; align-items: center; gap: 10px; }
  .contact svg { width: 15px; height: 15px; flex: none; }
  .figure {
    position: absolute;
    right: 40px; top: 30px;
    width: 210px; height: 370px;
    border-radius: 100px 100px 0 0;
    background: linear-gradient(180deg, var(--purple-soft), var(--purple-deep));
  }
</style>
</head>
<body>

<section class="card card-back">
  <div class="figure-faint" role="img" aria-label="Faint silhouette of a gymnast posing with arms outstretched"></div>
  <div class="monogram">CV</div>
  <div class="social-row">
    <span class="mark"></span><span>@VargaGym</span><span class="sep">|</span>
    <span class="mark"></span><span>@VargaGym</span><span class="sep">|</span>
    <span class="mark"></span><span>@CelestineVargaGymnasticsCenter</span>
  </div>
</section>

<section class="card card-front">
  <div class="brand">
    <div class="brand-mark">CV</div>
    <div class="brand-name">Celestine Varga<br>Gymnastics Center</div>
    <div class="brand-tagline">Tumbling, Clinics, Pilates &amp; More</div>
  </div>

  <div class="owner">
    <div class="owner-name">Celestine Varga</div>
    <div class="owner-role">Owner</div>
  </div>

  <ul class="contact">
    <li>
      <svg viewBox="0 0 16 16" aria-hidden="true"><path d="M3 1.5l3 .5 1 3-2 1.2a9 9 0 0 0 4.8 4.8L11 9l3 1 .5 3-2 1.5C7 14 2 9 1.5 3.5z" fill="none" stroke="#6b449b" stroke-width="1.5"/></svg>
      330-555-0192
    </li>
    <li>
      <svg viewBox="0 0 16 16" aria-hidden="true"><rect x="1" y="3" width="14" height="10" rx="1.5" fill="#6b449b"/><path d="M1.5 4l6.5 5 6.5-5" fill="none" stroke="#fff" stroke-width="1.3"/></svg>
      CelestineVargaGymnasticsCtr@mailbrook.com
    </li>
    <li>
      <svg viewBox="0 0 16 16" aria-hidden="true"><g fill="none" stroke="#6b449b" stroke-width="1.3"><circle cx="8" cy="8" r="6.5"/><ellipse cx="8" cy="8" rx="3" ry="6.5"/><path d="M1.5 8h13M2.5 4.8h11M2.5 11.2h11"/></g></svg>
      www.CelestineVargaGymnasticsCenter.com
    </li>
    <li>
      <svg viewBox="0 0 16 16" aria-hidden="true"><path d="M8 15s-5-5.5-5-9a5 5 0 0 1 10 0c0 3.5-5 9-5 9z" fill="#6b449b"/><circle cx="8" cy="6" r="1.8" fill="#fff"/></svg>
      918 S. Harlan Lane | Ashgrove, Indiana 44871
    </li>
  </ul>

  <div class="figure" role="img" aria-label="Purple silhouette of a gymnast reaching one arm up and one arm out"></div>
</section>

</body>
</html>
```